GUARANTEED! Simple website for independent event planner and consultant...

I need a website that is no more than 5 or 6 pages to illustrate who I am and what I can offer to groups who book hotels for meetings and conferences. I have 20 years of experience planning meetings within hotels and I am now ready to go out on my own and help clients choose venues, negotiate contracts and plan effective meetings. I will focus on clients planning meetings in the mountains of Colorado but I am willing to travel as well. I want to work with a person who is collaborative and can direct me on what they need to move the project along quickly. I already have my logo, a hosting site and work e-mail address. Also, I recently hired a photographer to do head shots. Lastly, it important for me to be able to talk on the phone or skype with this person, as needed and I must be able to make changes to my site down the road when necessary...

Target Market(s)

Corporate Groups

Industry/Entity Type

Event Planning

Coding

Coded - Design and coding required

Number of Pages Required

5+ page

Font styles to use
Sans Serif

Requirements
Must have
• About me page, event planning services offered page, task force and consulting work page, testimonials page, page for blogs, page to contact me/request a proposal. May need advice on what else I need...
Nice to have
• I want it to look sharp and professional. I want people to look at my site and know immediately that they can trust me and the work I can do.
• I don't want it to look like it is over the top as I am not a HUGE company but I do want it to be professional and easy to view and navigate.
Should not have
• Bright colors
• My logo is bright orange and black. I have also used dark grey and orange. See below:
• Orange:
• C = 0
• M = 64
• Y = 100
• K = 0
• Gray:
• C = 67
• M = 60
• Y = 59
• K = 45
• Font: Gotham Book and Gotham Bold

```html
<!DOCTYPE html>
<html lang="en">
<head>
<meta charset="utf-8">
<title>Services and Latest News</title>
<link rel="stylesheet" href="https://fonts.googleapis.com/css2?family=Poppins:wght@600;700&family=Lato:wght@400;700&display=swap">
<style>
  :root {
    --ink-dark: #4f4f4f;
    --ink-muted: #7d7d7d;
    --news-muted: #9aa2a8;
    --orange: #f47b20;
    --indigo: #2a2e96;
    --green: #1a9e63;
    --night: #232d35;
    --black: #0c0c0c;
    --white: #ffffff;
  }
  * { box-sizing: border-box; margin: 0; padding: 0; }
  html, body { width: 1200px; height: 535px; overflow: hidden; background: var(--white); }
  body { position: relative; font-family: "Lato", Arial, sans-serif; }

  .hero-strip { position: absolute; left: 0; top: 0; width: 1200px; height: 9.5px; background: var(--black); }
  .hero-photo { position: absolute; left: 259px; top: 0; width: 640px; height: 9.5px;
    background: linear-gradient(90deg, #6a6a6a, #a8a8a8 50%, #6e6e6e); }

  .services { position: absolute; left: 0; top: 9.5px; width: 1200px; height: 301.5px; text-align: center; }
  .section-title { font-family: "Poppins", Arial, sans-serif; font-weight: 700; font-size: 24px; letter-spacing: 0.5px; line-height: 1; }
  .services .section-title { position: absolute; top: 40px; left: 0; width: 100%; color: var(--ink-dark); }
  .section-lead { position: absolute; left: 0; width: 100%; font-size: 10.2px; line-height: 1; }
  .services .section-lead { top: 72px; color: var(--ink-muted); }

  .service { position: absolute; top: 125px; width: 229px; text-align: center; }
  .service--planning { left: 241.5px; }
  .service--collab { left: 489.5px; }
  .service--comms { left: 736.5px; }
  .service-icon { display: block; margin: 0 auto; width: 22px; height: 22px; }
  .service-name { font-family: "Poppins", Arial, sans-serif; font-weight: 700; font-size: 15.5px; line-height: 1; margin-top: 8px; }
  .service--planning .service-name { color: var(--orange); }
  .service--collab .service-name { color: var(--indigo); }
  .service--comms .service-name { color: var(--green); }
  .service-text { margin-top: 15px; font-size: 10.1px; line-height: 16.5px; color: var(--ink-muted); }

  .news { position: absolute; left: 0; top: 311px; width: 1200px; height: 224px; background: var(--night); text-align: center; }
  .news .section-title { position: absolute; top: 46px; left: 0; width: 100%; color: var(--white); font-size: 23px; }
  .news .section-lead { top: 78px; color: var(--news-muted); }
  .blog-button { position: absolute; left: 555px; top: 126px; width: 98px; height: 29px; background: var(--orange);
    color: var(--white); font-weight: 700; font-size: 10px; display: flex; align-items: center; justify-content: center; gap: 7px; text-decoration: none; }
  .blog-button svg { width: 10px; height: 10px; }
  .news-card { position: absolute; left: 242.5px; top: 206px; width: 228.5px; height: 20px; background: var(--white); }
</style>
</head>
<body>
  <header class="hero-strip">
    <div class="hero-photo" role="img" aria-label="Black and white photograph of a meeting venue"></div>
  </header>

  <section class="services">
    <h2 class="section-title">Services</h2>
    <p class="section-lead">In order to help you grow your business, our carefully selected experts can advise you in in the following areas:</p>

    <article class="service service--planning">
      <svg class="service-icon" viewBox="0 0 22 22" fill="none" stroke="#f47b20" stroke-width="1.6">
        <rect x="2" y="4" width="18" height="16" rx="1.5"/>
        <line x1="2" y1="8.5" x2="20" y2="8.5"/>
        <line x1="6.5" y1="2" x2="6.5" y2="6"/><line x1="15.5" y1="2" x2="15.5" y2="6"/>
        <line x1="6.5" y1="8.5" x2="6.5" y2="20" stroke-width="1"/><line x1="11" y1="8.5" x2="11" y2="20" stroke-width="1"/><line x1="15.5" y1="8.5" x2="15.5" y2="20" stroke-width="1"/>
        <line x1="2" y1="12.5" x2="20" y2="12.5" stroke-width="1"/><line x1="2" y1="16.3" x2="20" y2="16.3" stroke-width="1"/>
      </svg>
      <h3 class="service-name">Planning</h3>
      <p class="service-text">Consectetur adipiscing elit. Praesent molestie urna hendrerit erat tincidunt tempus. Aliquam a leo risus. Fusce a metus non augue dapibus porttitor at in mauris. Pellentesque commodo...</p>
    </article>

    <article class="service service--collab">
      <svg class="service-icon" viewBox="0 0 22 22" fill="#2a2e96">
        <path d="M20 3.5 L18.5 2 L14 6.5 L12.5 5 L12 10 L17 9.5 L15.5 8 Z"/>
        <path d="M2 18.5 L3.5 20 L8 15.5 L9.5 17 L10 12 L5 12.5 L6.5 14 Z"/>
      </svg>
      <h3 class="service-name">Collaboration</h3>
      <p class="service-text">Consectetur adipiscing elit. Praesent molestie urna hendrerit erat tincidunt tempus. Aliquam a leo risus. Fusce a metus non augue dapibus porttitor at in mauris. Pellentesque commodo...</p>
    </article>

    <article class="service service--comms">
      <svg class="service-icon" viewBox="0 0 22 22" fill="none" stroke="#1a9e63" stroke-width="1.8" stroke-linejoin="round">
        <path d="M9 3 C4.5 3 1.5 5.5 1.5 8.5 C1.5 10.2 2.5 11.6 4 12.6 L3.2 15.5 L6.6 13.8 C7.4 14 8.2 14.1 9 14.1 C13.5 14.1 16.5 11.6 16.5 8.5 C16.5 5.5 13.5 3 9 3 Z"/>
        <path d="M18 7.8 C19.6 8.8 20.5 10.2 20.5 11.8 C20.5 13.2 19.8 14.4 18.6 15.3 L19.3 18.3 L16 16.6 C15 16.9 14 17 13 16.9 C11.6 16.8 10.3 16.3 9.3 15.6" fill="#1a9e63" stroke="none"/>
      </svg>
      <h3 class="service-name">Communication</h3>
      <p class="service-text">Consectetur adipiscing elit. Praesent molestie urna hendrerit erat tincidunt tempus. Aliquam a leo risus. Fusce a metus non augue dapibus porttitor at in mauris. Pellentesque commodo...</p>
    </article>
  </section>

  <section class="news">
    <h2 class="section-title">Latest News</h2>
    <p class="section-lead">If you are interested in the latest articles in the industry, take a sneak peek at our blog. You have nothing to loose!</p>
    <a class="blog-button" href="#blog">
      <svg viewBox="0 0 10 10"><circle cx="5" cy="5" r="5" fill="#ffffff"/><path d="M4 2.8 L6.3 5 L4 7.2" fill="none" stroke="#f47b20" stroke-width="1.4"/></svg>
      See blog
    </a>
    <div class="news-card"></div>
  </section>
</body>
</html>
```